Real Estate For Sale Flyer Design Project

BrightOak Group of Realtors. We sell homes but want a more modern feel than the standard boring real estate flyers of the past. We want 8.5x11 flyers

Target Market(s)

mid level income home owners

Industry/Entity Type

Real Estate

Requirements
Must have
• fun

```html
<!DOCTYPE html>
<html lang="en">
<head>
<meta charset="utf-8">
<title>BrightOak Team – Your Dream Starts Here</title>
<link href="https://fonts.googleapis.com/css2?family=Montserrat:wght@400;600;700;800;900&family=Open+Sans:wght@400;600&display=swap" rel="stylesheet">
<style>
  :root {
    --purple: #6a2c7e;
    --purple-deep: #4e1d60;
    --lavender: #c89ad8;
    --ink: #333333;
    --muted: #555555;
    --white: #ffffff;
    --photo-sky: #9fb8cf;
    --photo-mid: #6f6a64;
    --photo-deck: #5a3d2b;
  }
  * { margin: 0; padding: 0; box-sizing: border-box; }
  html, body { width: 855px; height: 1200px; overflow: hidden; background: var(--white); }
  .flyer { position: relative; width: 855px; height: 1200px; overflow: hidden; background: var(--white); font-family: "Open Sans", Arial, sans-serif; color: var(--ink); }

  .hero { position: absolute; left: 0; top: 0; width: 855px; height: 640px; }
  .hero svg { display: block; }

  .headline {
    position: absolute; right: 20px; top: 30px; text-align: right;
    font-family: "Montserrat", Arial, sans-serif; font-weight: 900;
    font-size: 66px; line-height: 0.92; color: var(--white); letter-spacing: 1px;
  }

  .offer {
    position: absolute; left: 745px; top: 500px; width: 110px; white-space: nowrap;
    font-family: "Montserrat", Arial, sans-serif; color: var(--white);
  }
  .offer-save { font-size: 24px; font-weight: 600; line-height: 1.1; }
  .offer-amount { font-size: 27px; font-weight: 800; line-height: 1.15; }
  .offer-amount .pct { color: var(--lavender); }
  .offer-note { font-size: 13px; font-weight: 600; margin-top: 2px; }

  .features {
    position: absolute; left: 43px; top: 652px; width: 770px;
    display: grid; grid-template-columns: 1fr 1fr; column-gap: 40px; row-gap: 22px;
  }
  .feature-head { display: flex; align-items: center; gap: 10px; margin-bottom: 6px; }
  .feature-icon { width: 24px; height: 24px; flex: none; }
  .feature-title { font-family: "Montserrat", Arial, sans-serif; font-weight: 600; font-size: 18px; color: var(--ink); }
  .feature-body, .summary { font-size: 11.5px; line-height: 1.5; color: var(--muted); }

  .summary { position: absolute; left: 43px; top: 925px; width: 770px; }

  .brand { position: absolute; left: 43px; top: 1065px; display: flex; align-items: center; gap: 14px; }
  .brand-mark { width: 58px; height: 58px; border-radius: 50%; background: var(--purple); flex: none; }
  .brand-name { font-family: "Montserrat", Arial, sans-serif; font-weight: 800; font-size: 30px; color: var(--purple); line-height: 1; }
  .brand-tagline { font-size: 12px; color: var(--purple); margin-top: 6px; }

  .contact { position: absolute; left: 522px; top: 1058px; font-size: 16px; line-height: 1.9; color: var(--muted); }
</style>
</head>
<body>
<main class="flyer">
  <section class="hero">
    <svg width="855" height="640" viewBox="0 0 855 640">
      <defs>
        <linearGradient id="photoTone" x1="0" y1="0" x2="0" y2="1">
          <stop offset="0" stop-color="var(--photo-sky)"/>
          <stop offset="0.45" stop-color="var(--photo-mid)"/>
          <stop offset="1" stop-color="var(--photo-deck)"/>
        </linearGradient>
      </defs>
      <rect role="img" aria-label="Photo of a modern two-storey home with stone walls and a wooden deck at dusk" x="0" y="0" width="855" height="640" fill="url(#photoTone)"/>
      <path d="M0 625 C 260 615 520 570 855 450 L855 640 L0 640 Z" fill="var(--white)"/>
      <path d="M760 590 C 745 605 735 618 728 632 C 760 622 790 615 815 612 Z" fill="var(--purple-deep)"/>
      <circle cx="805" cy="552" r="80" fill="var(--purple)"/>
    </svg>
    <h1 class="headline">YOUR<br>DREAM<br>STARTS<br>HERE</h1>
    <div class="offer">
      <div class="offer-save">Save</div>
      <div class="offer-amount"><span class="pct">50%</span> off</div>
      <div class="offer-note">Discount Bar</div>
    </div>
  </section>

  <section class="features">
    <article class="feature">
      <div class="feature-head">
        <svg class="feature-icon" viewBox="0 0 26 26"><circle cx="13" cy="13" r="12" fill="none" stroke="var(--purple)" stroke-width="2"/><path d="M10 8 L16 13 L10 18" fill="none" stroke="var(--purple)" stroke-width="2.4"/></svg>
        <h2 class="feature-title">Your Heading Goes Here</h2>
      </div>
      <p class="feature-body">Lorem Ipsum is simply dummy text of the printing and typesetting industry. Lorem Ipsum has been the industry's standard dummy text ever since the 1500s, when an unknown printer took a galley of type and scrambled it to make a type specimen book. It has survived five centuries.</p>
    </article>
    <article class="feature">
      <div class="feature-head">
        <svg class="feature-icon" viewBox="0 0 26 26"><circle cx="13" cy="13" r="12" fill="none" stroke="var(--purple)" stroke-width="2"/><path d="M10 8 L16 13 L10 18" fill="none" stroke="var(--purple)" stroke-width="2.4"/></svg>
        <h2 class="feature-title">Your Heading Goes Here</h2>
      </div>
      <p class="feature-body">Lorem Ipsum is simply dummy text of the printing and typesetting industry. Lorem Ipsum has been the industry's standard dummy text ever since the 1500s, when an unknown printer took a galley of type and scrambled it to make a type specimen book. It has survived five centuries.</p>
    </article>
    <article class="feature">
      <div class="feature-head">
        <svg class="feature-icon" viewBox="0 0 26 26"><circle cx="13" cy="13" r="12" fill="none" stroke="var(--purple)" stroke-width="2"/><path d="M10 8 L16 13 L10 18" fill="none" stroke="var(--purple)" stroke-width="2.4"/></svg>
        <h2 class="feature-title">Your Heading Goes Here</h2>
      </div>
      <p class="feature-body">Lorem Ipsum is simply dummy text of the printing and typesetting industry. Lorem Ipsum has been the industry's standard dummy text ever since the 1500s, when an unknown printer took a galley of type and scrambled it to make a type specimen book. It has survived five centuries.</p>
    </article>
    <article class="feature">
      <div class="feature-head">
        <svg class="feature-icon" viewBox="0 0 26 26"><circle cx="13" cy="13" r="12" fill="none" stroke="var(--purple)" stroke-width="2"/><path d="M10 8 L16 13 L10 18" fill="none" stroke="var(--purple)" stroke-width="2.4"/></svg>
        <h2 class="feature-title">Your Heading Goes Here</h2>
      </div>
      <p class="feature-body">Lorem Ipsum is simply dummy text of the printing and typesetting industry. Lorem Ipsum has been the industry's standard dummy text ever since the 1500s, when an unknown printer took a galley of type and scrambled it to make a type specimen book. It has survived five centuries.</p>
    </article>
  </section>

  <p class="summary">Lorem Ipsum is simply dummy text of the printing and typesetting industry. Lorem Ipsum has been the industry's standard dummy text ever since the 1500s, when an unknown printer took a galley of type and scrambled it to make a type specimen book. It has survived not only five centuries, but also the leap into electronic typesetting, remaining essentially unchanged. Lorem Ipsum is simply dummy text of the printing and typesetting industry. Lorem Ipsum has been the industry's standard dummy text ever since the 1500s, when an unknown printer took a galley of type and scrambled it to make a type specimen book. It has survived five centuries.</p>

  <footer>
    <div class="brand">
      <div class="brand-mark"></div>
      <div>
        <div class="brand-name">BrightOak Team</div>
        <div class="brand-tagline">Your home, your next great chapter</div>
      </div>
    </div>
    <div class="contact">
      <div>Address</div>
      <div>Phone</div>
    </div>
  </footer>
</main>
</body>
</html>
```